Startup FinTech / Behavioural Science company needs website redesign

We are a startup company interested in redesigning our website. We have most of our content created already (viewable at www.tallowmint.example), but are interested in an upgraded look and feel. We are happy to adjust content as well based on design input. We will move hosting from brixelpad to hostvarra or similar hosting service, so portability of files is important to us. Our team will have the ability to make minor tweaks/content adjustments, but would look to engage with someone for more-comprehensive enhancements in the future.
Updates

Reason: Other business needs prevented me from providing timely feedback. I will work on feedback over the next two days but wanted to give additional time for design submissions and revisions.

Target Market(s)

Financial advisors in the US and UK, as well as potential end-users of the tools and potential investors

Industry/Entity Type

Information Technology

Coding

Coded - Design and coding required

Number of Pages Required

1 page

Font styles to use
Sans Serif

Requirements
Must have
• - Lighter, cleaner look and feel. We believe our current website is too heavy and "angular."
• - improved iconography to convey behavioural finance concepts (e.g., herd mentality, and illusion of control)
• - links to social media sites
• - integration with our brixelpad personality profile (viewable now at https://lenaobisk.formquill.example/to/qZ7mRt. Note: we will change this URL to tallowmint.formquill.example... as a part of the design process)
Nice to have
• - ability for us to add a tab/link to a blog in the future.
• - design that allows us to add additional
• - ability for us to add additional pages (e.g., results from our personality profiles, pages to customize sharing on social media)
• - simple ability to enter an email address to add to our mailing list/request more info
• - mobile-responsive design
Should not have
• - Should not have items like office directions and maps, since we are a virtual team.
• - Contact information (e.g., phone number) should be lower down the page vs. at the top
• - comments boxes or lengthy web forms. A simple name/email address is sufficient.

```html
<!DOCTYPE html>
<html lang="en">
<head>
<meta charset="utf-8">
<title>tallowmint – Money decisions made calmer</title>
<link rel="stylesheet" href="https://fonts.googleapis.com/css2?family=Raleway:wght@400;500;600;700;800&family=Lato:wght@400;700&display=swap">
<style>
:root{
  --purple:#8b1fa0;
  --purple-deep:#6d1583;
  --ink:#111111;
  --text:#555555;
  --grey-band:#f2f2f2;
  --dark:#2f2f2f;
  --white:#ffffff;
}
*{box-sizing:border-box;margin:0;padding:0}
html,body{width:1200px;height:3854px;overflow:hidden}
body{font-family:'Lato',Arial,sans-serif;color:var(--text);background:var(--white)}
h1,h2,h3,h4{font-family:'Raleway',Arial,sans-serif}
a{color:inherit;text-decoration:none}
header,section,footer{position:relative;width:1200px;overflow:hidden}

/* hero */
.hero{height:676px}
.hero-scene{position:absolute;inset:0;background:linear-gradient(180deg,#cfe6f6 0%,#e9f4fb 45%,#7fc3dc 64%,#f3efe6 74%,#fbfaf6 100%)}
.site-nav{position:absolute;left:0;top:0;width:1200px;height:77px}
.brand{position:absolute;left:77px;top:12px;font-family:'Raleway',sans-serif;font-weight:700;font-size:44px;color:var(--purple-deep);letter-spacing:-0.5px}
.nav-links{list-style:none;font-size:13px;color:#222}
.nav-links li{position:absolute;top:38px;white-space:nowrap}
.nav-links li:nth-child(1){left:547px;color:var(--purple)}
.nav-links li:nth-child(2){left:683px}
.nav-links li:nth-child(3){left:817px}
.nav-links li:nth-child(4){left:933px}
.nav-links li:nth-child(5){left:1063px}
.hero-copy{position:absolute;left:620px;top:212px;color:var(--ink)}
.hero-copy h1{font-size:56px;font-weight:700;line-height:64px;letter-spacing:-0.5px}
.hero-copy .tagline{font-family:'Raleway',sans-serif;font-size:50px;font-weight:400;margin-top:12px;line-height:56px}
.hero-copy .tagline b{color:var(--purple);font-weight:400}
.hero-copy .advisor{font-size:20px;font-weight:700;margin-top:8px}
.hero-copy .advisor a{text-decoration:underline}
.btn{display:inline-flex;align-items:center;justify-content:center;font-family:'Raleway',sans-serif;font-weight:700}
.btn-start{position:absolute;left:620px;top:496px;width:241px;height:46px;background:var(--purple);color:#fff;font-size:17px;border-radius:3px}

/* problem */
.problem{height:249px;text-align:center}
.section-title{font-size:46px;font-weight:800;color:var(--ink);letter-spacing:0.5px;line-height:54px}
.section-title span{color:var(--purple)}
.problem .section-title{padding-top:50px}
.problem p{font-size:15px;line-height:23px;width:880px;margin:12px auto 0}
.why{height:262px;background:var(--grey-band);text-align:center;padding-top:52px}
.why p{font-size:15px;line-height:23px;width:880px;margin:0 auto 18px}
.why h4{font-size:20px;font-weight:700;color:var(--ink)}

/* bias cards */
.biases{height:265px;background:linear-gradient(180deg,var(--grey-band) 0,var(--grey-band) 36px,#fff 36px)}
.bias-row{position:absolute;left:77px;top:0;width:1046px;height:255px;display:flex;box-shadow:0 14px 18px -10px rgba(0,0,0,.35)}
.bias-card{flex:1;display:flex;flex-direction:column;align-items:center;justify-content:flex-end;padding-bottom:58px;color:#fff;text-align:center;font-size:19px;line-height:24px}
.bias-card small{display:block;font-size:14px;line-height:20px;margin-top:6px;width:200px;margin-bottom:-44px}
.bias-card.dark{background:linear-gradient(160deg,#4a4a4a,#2a2a2a)}
.bias-card.herd{background:linear-gradient(160deg,#8a3aa0,#6b1d80)}
.bias-card.gamble{background:linear-gradient(160deg,#9d6cab,#7a4a8c)}
.bias-card.control{background:linear-gradient(160deg,#9b35b0,#7a1d92)}

.intro-solution{height:247px;text-align:center;padding-top:58px}
.intro-solution p{font-family:'Raleway',sans-serif;font-weight:700;font-size:20px;color:var(--ink)}
.intro-solution svg{display:block;margin:16px auto 0}
.intro-solution .section-title{margin-top:18px}

/* solutions */
.solutions{height:796px;display:grid;grid-template-columns:600px 600px;grid-template-rows:398px 398px}
.step{position:relative;text-align:center;color:#fff;padding-top:58px}
.step.p1{background:linear-gradient(135deg,#9a3cb0,#741e8a)}
.step.d1{background:linear-gradient(135deg,#4d4d4d,#2d2d2d)}
.step.d2{background:linear-gradient(135deg,#5a5a5a,#343434)}
.step.p2{background:linear-gradient(135deg,#9330ab,#6f1a86)}
.step-icon{width:100px;height:100px;border:3px solid #fff;border-radius:50%;margin:0 auto;display:flex;align-items:center;justify-content:center}
.step h3{font-size:34px;font-weight:700;margin-top:38px;letter-spacing:0.3px;line-height:40px}
.step p{font-size:15px;line-height:21px;width:470px;margin:8px auto 0}
.step .btn{margin-top:20px;width:156px;height:48px;background:#fff;color:var(--purple-deep);font-size:15px;border-radius:2px}

/* team */
.team{height:383px;background:var(--purple)}
.team .section-title{color:#fff;font-size:38px;text-align:center;padding-top:52px}
.member{position:absolute;top:132px;width:330px;height:220px}
.member .avatar{position:absolute;left:0;top:0;width:150px;height:150px;border-radius:50%;border:5px solid #fff;background:radial-gradient(circle at 50% 40%,#c9b7a6,#6c5d55)}
.member .info{position:absolute;left:165px;top:0;width:165px;color:#fff;font-size:12.5px;line-height:17px}
.member h4{font-size:20px;font-weight:700;line-height:22px;margin-bottom:8px}
.member .social{position:absolute;left:59px;top:170px;width:32px;height:32px;border:2px solid #fff;border-radius:50%}
.m1{left:82px}.m2{left:437px}.m3{left:792px}

/* take profile */
.take-profile{height:365px;text-align:center;color:#fff}
.take-profile .bg{position:absolute;inset:0;background:linear-gradient(135deg,#6f6f6f,#3a3a3a 55%,#555)}
.take-profile .content{position:relative}
.take-profile h2{font-size:44px;font-weight:600;padding-top:78px;letter-spacing:0.5px;line-height:52px}
.take-profile p{font-size:26px;margin-top:10px;font-family:'Raleway',sans-serif}
.take-profile .btn{margin-top:24px;width:224px;height:59px;background:var(--purple);font-size:19px;border-radius:3px;gap:12px}

/* newsletter */
.newsletter{height:288px;text-align:center}
.newsletter .section-title{font-size:38px;padding-top:50px;font-weight:700;line-height:46px}
.newsletter p{font-size:14px;line-height:22px;width:560px;margin:10px auto 0}
.subscribe{position:absolute;left:313px;top:180px;display:flex;gap:10px}
.subscribe .field{width:417px;height:51px;border:1px solid #ccc;display:flex;align-items:center;padding-left:22px;font-size:13px;color:#999}
.subscribe .btn{width:147px;height:51px;background:var(--purple);color:#fff;font-size:14px}

/* footer */
.site-footer{height:259px;background:var(--purple);color:#fff}
.footer-brand{position:absolute;left:62px;top:104px;display:flex;align-items:center;gap:12px;font-family:'Raleway',sans-serif;font-weight:700;font-size:34px}
.footer-brand i{width:26px;height:26px;border-radius:50%;background:#fff}
.f-col{position:absolute;top:34px;font-size:14px;line-height:26px}
.f-col h4{font-family:'Raleway',sans-serif;font-weight:500;font-size:20px;margin-bottom:12px}
.f-col ul{list-style:none}
.col-links{left:350px}.col-quote{left:620px;width:230px}.col-contact{left:892px}
.col-quote p{font-size:14px;line-height:22px}
.quote-nav{display:flex;gap:8px;margin-top:14px}
.quote-nav span{width:34px;height:34px;background:#fff;display:flex;align-items:center;justify-content:center}
.col-contact li{display:flex;align-items:center;gap:10px}
.socials{position:absolute;left:892px;top:178px;display:flex;gap:22px}
.socials span{width:50px;height:50px;border-radius:50%;background:#fff}
.socials span:first-child{background:#1a1a1a}
.bottom-bar{height:64px;background:var(--dark);color:#ddd;font-size:14px;display:flex;align-items:center;justify-content:space-between;padding:0 80px}
</style>
</head>
<body>

<header class="hero">
  <div class="hero-scene" role="img" aria-label="Photo: two people relaxing in deck chairs under a yellow beach umbrella by the sea"></div>
  <nav class="site-nav">
    <a class="brand" href="#">tallowmint</a>
    <ul class="nav-links">
      <li>The Problem</li><li>The Solution</li><li>Our Team</li><li>Take Profile</li><li>Contact</li>
    </ul>
  </nav>
  <div class="hero-copy">
    <h1>Money Decisions<br>can Stress you Out</h1>
    <div class="tagline"><b>tallowmint</b> can HELP!</div>
    <div class="advisor">are you a financial advisor? <a href="#">click here</a></div>
  </div>
  <a class="btn btn-start" href="#">Let's Start Now</a>
</header>

<section class="problem">
  <h2 class="section-title">THE <span>PROBLEM</span></h2>
  <p>Money and financial issues are the leading causes of anxiety for most of us. This financial stress is among the leading causes of divorce, addiction, obesity and depression.<br>What's worse, the consequences of the decisions that we make can make us even more stressed, not more relieved.</p>
</section>

<section class="why">
  <p>Ask anyone the key to good physical health, and you're likely to get a correct answer: don't overeat, choose healthy foods and exercise regularly. The path to good physical health is not a mystery, but we have a hard time following it.</p>
  <p>Good financial health works the same way. We generally know what to do – spend less than we earn, save for a rainy day, and make non-emotional investment decisions – but have a hard time doing it.</p>
  <h4>Why?</h4>
</section>

<section class="biases">
  <div class="bias-row">
    <div class="bias-card dark">Short-term Thinking<small>Lorem Ipsum is simply dummy text for printing »</small></div>
    <div class="bias-card herd">Herd Mentality</div>
    <div class="bias-card gamble">Gambler's Fallacy</div>
    <div class="bias-card control">Illusion of Control</div>
  </div>
</section>

<section class="intro-solution">
  <p>This is where tallowmint comes in.</p>
  <svg width="22" height="22" viewBox="0 0 22 22" fill="none" stroke="#111" stroke-width="2.5"><path d="M3 3l8 7 8-7M3 11l8 7 8-7"/></svg>
  <h2 class="section-title">THE <span>SOLUTION</span></h2>
</section>

<section class="solutions">
  <div class="step p1">
    <div class="step-icon"><svg width="40" height="46" viewBox="0 0 40 46" fill="none" stroke="#fff" stroke-width="3"><rect x="4" y="5" width="32" height="38" rx="3"/><path d="M12 18h16M12 26h16M12 34h10"/></svg></div>
    <h3>TAKE THE PROFILE</h3>
    <p>Take the tallowmint profile to learn more about your financial personality and tendencies</p>
    <a class="btn" href="#">CLICK HERE</a>
  </div>
  <div class="step d1">
    <div class="step-icon"><svg width="46" height="46" viewBox="0 0 46 46" fill="none" stroke="#fff" stroke-width="3"><path d="M8 38l8-8M30 16l8-8M20 14l12 12-6 6-12-12z"/></svg></div>
    <h3>CONNECT YOUR ACCOUNTS</h3>
    <p>Connect your financial accounts to see your opportunities to be a better saver and investor</p>
    <a class="btn" href="#">CONNECT NOW</a>
  </div>
  <div class="step d2">
    <div class="step-icon"><svg width="46" height="46" viewBox="0 0 46 46" fill="none" stroke="#fff" stroke-width="3"><circle cx="23" cy="23" r="18" stroke-dasharray="8 5"/><path d="M14 23l7 7 12-14"/></svg></div>
    <h3>CHECK YOUR PROGRESS</h3>
    <p>Check your progress over time to stay on track</p>
    <a class="btn" href="#">CLICK HERE</a>
  </div>
  <div class="step p2">
    <div class="step-icon"><svg width="46" height="46" viewBox="0 0 46 46" fill="none" stroke="#fff" stroke-width="3"><circle cx="20" cy="20" r="11"/><path d="M28 28l11 11"/></svg></div>
    <h3>GAIN BETTER INSIGHT</h3>
    <p>receive valuable coaching to learn how your personality affects your financial decision making</p>
    <a class="btn" href="#">LEARN MORE</a>
  </div>
</section>

<section class="team">
  <h2 class="section-title">OUR TEAM</h2>
  <div class="member m1">
    <div class="avatar" role="img" aria-label="Portrait photo of Lena Obisk"></div>
    <div class="info"><h4>Lena Obisk,<br>CFA</h4>CEO<br>FinTech Veteran<br>Investment Portfolio<br>Manager<br>Thamesbrook Business School<br>Harlow Mellick<br>University</div>
    <span class="social"></span>
  </div>
  <div class="member m2">
    <div class="avatar" role="img" aria-label="Portrait photo of Marco Tellsen"></div>
    <div class="info"><h4>Marco Tellsen</h4>CTO<br>Data Science Expert<br>Predictive Analytics<br>Solution Architect<br>Westridge University<br>University of Calverton</div>
    <span class="social"></span>
  </div>
  <div class="member m3">
    <div class="avatar" role="img" aria-label="Portrait photo of Dorian Vasquell"></div>
    <div class="info"><h4>Dorian<br>Vasquell, PhD</h4>Chief Data Scientist<br>Decision Analysis Expert<br>Statistical Modeling<br>Solution Architect<br>Fernvale University<br>Harlow Mellick<br>University</div>
    <span class="social"></span>
  </div>
</section>

<section class="take-profile">
  <div class="bg" role="img" aria-label="Photo: laptop showing financial charts on a desk, darkened"></div>
  <div class="content">
    <h2>TAKE PROFILE</h2>
    <p>Want to learn about your financial personality?</p>
    <a class="btn" href="#"><svg width="22" height="22" viewBox="0 0 22 22" fill="none" stroke="#fff" stroke-width="2.2"><circle cx="11" cy="11" r="8"/><path d="M7 11l3 3 5-6"/></svg>CLICK HERE</a>
  </div>
</section>

<section class="newsletter">
  <h2 class="section-title">NEWSLETTER <span>SUBSCRIPTION</span></h2>
  <p>Subscribe to our Newsletter and get Latest News &amp; Updates. Join Our amazing Workshops &amp; Training to know much more</p>
  <div class="subscribe">
    <div class="field">E-mail</div>
    <a class="btn" href="#">SUBSCRIBE</a>
  </div>
</section>

<footer class="site-footer">
  <div class="footer-brand"><i></i>tallowmint</div>
  <div class="f-col col-links">
    <h4>Useful Links</h4>
    <ul><li>Home</li><li>The Problem</li><li>The Solution</li><li>Our Team</li><li>Take Profile</li><li>Contact</li></ul>
  </div>
  <div class="f-col col-quote">
    <h4>Client Testimonial</h4>
    <p>Lorem Ipsum is simply dummy text of the printing and typesetting industry...</p>
    <p><b>- Client Name</b></p>
    <div class="quote-nav">
      <span><svg width="12" height="14" viewBox="0 0 12 14"><path d="M10 1L2 7l8 6z" fill="#6d1583"/></svg></span>
      <span><svg width="12" height="14" viewBox="0 0 12 14"><path d="M2 1l8 6-8 6z" fill="#6d1583"/></svg></span>
    </div>
  </div>
  <div class="f-col col-contact">
    <h4>Get In Touch With Us</h4>
    <ul>
      <li><svg width="16" height="16" viewBox="0 0 16 16"><path d="M3 1l3 3-2 2c1 2 3 4 5 5l2-2 3 3-2 3C7 15 1 9 1 3z" fill="#fff"/></svg>+1 555 014 2290</li>
      <li><svg width="16" height="16" viewBox="0 0 16 16"><path d="M3 1l3 3-2 2c1 2 3 4 5 5l2-2 3 3-2 3C7 15 1 9 1 3z" fill="#fff"/></svg>+44 7700 900 418</li>
      <li><svg width="16" height="16" viewBox="0 0 16 16" fill="none" stroke="#fff" stroke-width="1.5"><rect x="1" y="3" width="14" height="10"/><path d="M1 3l7 6 7-6"/></svg>hello@tallowmint.example</li>
    </ul>
  </div>
  <div class="socials"><span></span><span></span><span></span></div>
</footer>

<div class="bottom-bar"><span>© TALLOWMINT - 2017. All Rights Reserved.</span><span>Privacy Policy</span></div>

</body>
</html>
```